Modern corporate energy/fuel business need business card design

Business card required for company founder. Korvan Fuel Co. is a Australian based modern energy/fuel provider. We offer specialised solutions to businesses using fossil fuels through renewable energy solutions.

I would like one side with specific information (name, address etc)

The other side to be bold, professional company name & logo. Striking.

Target Market(s)

B2B. Transport, mining, councils, environmentalist,

Industry/Entity Type

Petroleum

Contact Information for Business Card

Name; Peter Morrow
Position; Director
Email; pmorrow@korvanfuel.com.au
Address; PO Box 347, Larkvale, NSW, 2963
Website; www.korvanfuel.com.au

Colors

Designer to choose colors to be used in the design.

Requirements
Must have
• Clean, easy to read, professional & strong theme
Should not have
• too many colours, busy layout,

```html
<!DOCTYPE html>
<html lang="en">
<head>
<meta charset="utf-8">
<title>Korvan Fuel Co. – Business Card</title>
<link href="https://fonts.googleapis.com/css2?family=Lato:wght@400;700&display=swap" rel="stylesheet">
<style>
  :root {
    --backdrop: #ececec;
    --card-white: #ffffff;
    --navy: #1d4466;
    --orange: #f37a2c;
    --orange-deep: #ec3b24;
    --orange-light: #f8a048;
    --text-grey: #3b3b3b;
  }
  * { box-sizing: border-box; margin: 0; padding: 0; }
  html, body {
    width: 1200px; height: 900px; overflow: hidden;
    background: var(--backdrop);
    font-family: "Lato", Arial, sans-serif;
  }
  .sheet {
    width: 1200px; height: 900px;
    display: flex; flex-direction: column;
    align-items: center; justify-content: center; gap: 56px;
  }
  .card {
    width: 640px; height: 366px; position: relative; overflow: hidden;
    box-shadow: 0 6px 18px rgba(0,0,0,0.12);
  }

  /* Information side */
  .card--info { background: var(--card-white); }
  .brand {
    position: absolute; left: 48px; top: 58px;
    display: flex; align-items: center; gap: 12px;
  }
  .brand__dot { width: 38px; height: 38px; border-radius: 50%; background: var(--orange); flex: none; }
  .brand__name { font-size: 22px; font-weight: 700; color: var(--navy); letter-spacing: 0.5px; white-space: nowrap; }
  .person { position: absolute; right: 48px; top: 58px; text-align: right; }
  .person__name { font-size: 24px; font-weight: 700; color: var(--navy); line-height: 1.1; }
  .person__role { font-size: 15px; color: var(--orange); margin-top: 2px; }
  .divider {
    position: absolute; left: 48px; right: 48px; top: 150px;
    height: 2px; background: var(--orange); opacity: 0.85;
  }
  .contacts { position: absolute; left: 48px; bottom: 58px; list-style: none; }
  .contacts li {
    display: flex; align-items: center; gap: 10px;
    font-size: 15px; color: var(--text-grey); line-height: 27px;
  }
  .contacts svg { width: 15px; height: 15px; fill: var(--orange); flex: none; }
  .address {
    position: absolute; right: 48px; top: 176px; text-align: right;
    font-size: 15px; color: var(--text-grey); line-height: 24px; font-style: normal;
  }

  /* Brand side */
  .card--brand {
    background: linear-gradient(30deg, var(--orange-deep) 0%, var(--orange) 55%, var(--orange-light) 100%);
  }
  .brand--hero {
    position: absolute; left: 50%; top: 50%; transform: translate(-50%, -50%);
    gap: 18px;
  }
  .brand--hero .brand__dot { width: 62px; height: 62px; background: #ffffff; }
  .brand--hero .brand__name { font-size: 40px; color: #ffffff; letter-spacing: 1px; }
</style>
</head>
<body>
<main class="sheet">
  <section class="card card--info">
    <div class="brand">
      <span class="brand__dot"></span>
      <span class="brand__name">Korvan Fuel Co.</span>
    </div>
    <div class="person">
      <p class="person__name">Peter Morrow</p>
      <p class="person__role">Director</p>
    </div>
    <div class="divider"></div>
    <address class="address">PO Box 347, Larkvale<br>NSW, 2963</address>
    <ul class="contacts">
      <li>
        <svg viewBox="0 0 24 24"><path d="M6.6 10.8a15.1 15.1 0 0 0 6.6 6.6l2.2-2.2a1 1 0 0 1 1-.25 11.4 11.4 0 0 0 3.6.57 1 1 0 0 1 1 1V20a1 1 0 0 1-1 1A17 17 0 0 1 3 4a1 1 0 0 1 1-1h3.5a1 1 0 0 1 1 1c0 1.25.2 2.45.57 3.57a1 1 0 0 1-.25 1z"/></svg>
        +61 400 555 019
      </li>
      <li>
        <svg viewBox="0 0 24 24"><path d="M2 5h20v2l-10 6L2 7zM2 9l10 6 10-6v10H2z"/></svg>
        pmorrow@korvanfuel.com.au
      </li>
      <li>
        <svg viewBox="0 0 24 24"><circle cx="12" cy="12" r="10"/><path d="M2 12h20M12 2c3 3 3 17 0 20M12 2c-3 3-3 17 0 20" stroke="#fff" stroke-width="1.5" fill="none"/></svg>
        www.korvanfuel.com.au
      </li>
    </ul>
  </section>

  <section class="card card--brand">
    <div class="brand brand--hero">
      <span class="brand__dot"></span>
      <span class="brand__name">Korvan Fuel Co.</span>
    </div>
  </section>
</main>
</body>
</html>
```